Creative Brief
Cedar Brook Emergency Center
Web Site
Health
www.CedarBrookER.example
We are the first Free Standing Emergency Room in Dallas! We have all the advantages of a hospital based ER without the hassle or wait. Add in customer service and a aesthetic environment and you will see what makes us so unique for you emergent medical needs.
Our free standing ER solution provides
No wait emergency rooms!
Open 24 hours a day, 7 days a week
State of the art equipment and diagnosing capabilities
All our doctors are trained Emergency Medicine physicians
Experienced friendly nurses
Onsite emergent radiology (x-rays, CAT scans, Ultrasound)
Onsite emergent laboratory with result within minutes
I like a clean website- not too busy. Needs to be professional. A few nice pictures representing emergency medicine. I do not want things that are overused like pictures of a heart or EKG strip. Please incorporate the logo and from the logo you can see they colors and fonts that I like
left side
I do not have any specific web sites that i like or dislike and am open to many options.
web content

```html
<!DOCTYPE html>
<html lang="en">
<head>
<meta charset="utf-8">
<title>Cedar Brook Emergency Center</title>
<link href="https://fonts.googleapis.com/css2?family=Arimo:ital,wght@0,400;0,700;1,700&display=swap" rel="stylesheet">
<style>
:root{
  --red:#d3181e;
  --red-dark:#9e1014;
  --charcoal:#2b2b2b;
  --charcoal-2:#3a3a3a;
  --ink:#333;
  --muted:#666;
  --page:#f1f1f1;
  --line:#d8d8d8;
  --yellow:#f6c400;
  --orange:#f08a00;
  --pink:#f4c9c9;
}
*{box-sizing:border-box;margin:0;padding:0}
html,body{width:1200px;height:1018px;overflow:hidden}
body{position:relative;background:var(--page);font-family:"Arimo",Arial,sans-serif;color:var(--ink)}
.abs{position:absolute}

/* backdrop */
.backdrop{position:absolute;left:0;top:0;width:1200px;height:1018px}

/* header */
.brand{left:221px;top:30px;display:flex;align-items:center;gap:14px}
.brand-dot{width:60px;height:60px;border-radius:50%;background:var(--red)}
.brand-name{color:var(--red);font-weight:700;font-size:22px;line-height:24px;text-transform:uppercase;letter-spacing:.5px}
.social{left:567px;top:6px;display:flex;gap:8px}
.social span{width:24px;height:24px;border-radius:4px;background:#4d7fb8}
.call-tab{left:690px;top:0;width:294px;height:52px;background:var(--red);border-radius:0 0 14px 14px;color:#fff;text-align:center;padding-top:6px}
.call-tab .phone{font-size:19px;font-weight:700;font-style:italic}
.call-tab .mail{font-size:12px;font-weight:700;margin-top:3px}
.nav{left:540px;top:72px;width:444px;height:32px;background:var(--charcoal);border-radius:6px;display:flex;align-items:center;justify-content:space-around;padding:0 6px}
.nav a{color:#fff;text-decoration:none;font-size:11px;text-transform:uppercase;padding:6px 9px;border-radius:4px}
.nav a.active{background:var(--red)}

/* hero */
.hero{left:221px;top:116px;width:763px;height:252px;background:#fff;border:4px solid #fff;border-radius:8px;box-shadow:0 2px 8px rgba(0,0,0,.2);overflow:hidden}
.hero-photo{position:absolute;left:0;top:0;width:470px;height:244px;background:linear-gradient(100deg,#dfe6ea,#f4f4f2 55%,#c9d6de)}
.hero-copy{position:absolute;left:480px;top:62px;width:275px;text-align:center}
.hero-copy .soon{color:var(--red);font-size:38px}
.hero-copy .line{color:var(--ink);font-size:34px;line-height:42px}
.slider-dots{left:574px;top:383px;display:flex;gap:8px}
.slider-dots i{width:9px;height:9px;border-radius:50%;background:#bbb}
.slider-dots i.on{background:var(--red)}

/* main */
.welcome-title{left:221px;top:420px;font-size:24px;font-weight:700;display:flex;align-items:center;gap:10px}
.welcome-title::before{content:"";width:14px;height:14px;background:var(--red)}
.welcome-title em{font-style:normal;color:var(--red)}
.welcome-photo{left:221px;top:462px;width:84px;height:98px;background:linear-gradient(160deg,#c9b49c,#e8e1d8);border:3px solid #fff;box-shadow:0 1px 4px rgba(0,0,0,.3)}
.copy{font-size:11.5px;line-height:17px;color:var(--muted)}
.copy-intro{left:318px;top:462px;width:423px}
.copy-more{left:221px;top:566px;width:520px}
.rule{left:221px;top:670px;width:520px;border-top:1px dashed var(--line)}
.solution-title{left:221px;top:686px;font-size:19px;font-weight:700;font-style:italic;color:var(--red-dark)}
.features{left:221px;top:728px;list-style:none}
.features li{display:flex;align-items:center;gap:10px;height:30px;font-size:12px;color:var(--ink)}
.features svg{flex:none}
.badge{left:548px;top:760px;width:190px;text-align:center}
.badge .big{font-size:92px;font-weight:700;font-style:italic;color:var(--red);line-height:92px;letter-spacing:-3px}
.badge .small{font-size:19px;font-weight:700;font-style:italic;color:var(--orange);line-height:20px}

/* sidebar */
.side-rule{left:758px;top:420px;height:510px;border-left:1px solid var(--line)}
.side-title{left:780px;top:424px;font-size:20px;font-weight:700;display:flex;align-items:center;gap:10px}
.news-title{left:780px;top:466px;width:204px;font-size:12px;font-weight:700;color:var(--red);line-height:16px}
.news-date{left:780px;top:506px;font-size:11px;font-weight:700}
.news-text{left:780px;top:528px;width:204px}
.read-more{left:920px;top:582px;background:var(--red);color:#fff;font-size:10px;padding:4px 8px;border-radius:3px}
.map{left:780px;top:628px;width:204px;height:154px;background:linear-gradient(135deg,#e7ecdf,#f3f1ea 50%,#dfe7ef);border:1px solid var(--line)}
.field{left:780px;width:204px;height:28px;border:1px solid #ccc;background:#fff;font-size:11px;color:var(--muted);padding:7px 8px}
.field.name{top:840px}
.field.mail{top:882px}
.submit{left:920px;top:924px;width:64px;height:22px;background:var(--yellow);font-size:11px;font-weight:700;text-align:center;line-height:22px;border-radius:3px}

/* footer */
.footer-links{left:0;top:964px;width:1200px;text-align:center;font-size:12px;color:#fff}
.footer-links span{margin:0 6px;color:#999}
.copyright{left:0;top:990px;width:1200px;text-align:center;font-size:9px;color:#aaa}
</style>
</head>
<body>

<svg class="backdrop" viewBox="0 0 1200 1018" aria-hidden="true">
  <defs>
    <radialGradient id="glow" cx="50%" cy="0%" r="75%">
      <stop offset="0" stop-color="#f8d6d6"/>
      <stop offset="1" stop-color="#f1f1f1"/>
    </radialGradient>
  </defs>
  <rect width="1200" height="430" fill="url(#glow)"/>
  <path d="M0 0H1200V60Q600 20 0 60Z" fill="#3a3a3a" opacity=".9"/>
  <path d="M0 1018V970Q600 930 1200 970V1018Z" fill="#2b2b2b"/>
</svg>

<header>
  <div class="abs brand">
    <div class="brand-dot"></div>
    <div class="brand-name">Cedar Brook<br>Emergency Center</div>
  </div>
  <div class="abs social"><span></span><span></span><span></span></div>
  <div class="abs call-tab">
    <div class="phone">Call Us Today: 555-014-2290</div>
    <div class="mail">info@cedarbrook.example</div>
  </div>
  <nav class="abs nav">
    <a class="active" href="#">Home</a><a href="#">About Us</a><a href="#">Services</a><a href="#">FAQ</a><a href="#">Contact/Location</a><a href="#">For Provider</a>
  </nav>
</header>

<section class="abs hero">
  <div class="hero-photo" role="img" aria-label="Photo of smiling doctors reviewing a chart"></div>
  <div class="hero-copy">
    <div class="soon">Opening soon!</div>
    <div class="line">look for us to</div>
    <div class="line">open winter 2011</div>
  </div>
</section>
<div class="abs slider-dots"><i></i><i></i><i class="on"></i><i></i><i></i></div>

<main>
  <h1 class="abs welcome-title">Welcome to&nbsp;<em>CEDAR BROOK</em></h1>
  <div class="abs welcome-photo" role="img" aria-label="Photo of a family at the emergency center"></div>
  <p class="abs copy copy-intro">We are the first free standing emergency room in Dallas, with all the care of a hospital based ER and none of the long wait. Our team is ready day and night to treat you and your family quickly, calmly and with respect. Walk in at any hour and a trained emergency physician will see you in minutes, not hours.</p>
  <p class="abs copy copy-more">Our building was designed to feel calm and welcoming, from the quiet waiting area to the private treatment rooms. Imaging and lab results are ready on site, so decisions are made fast and you head home sooner. We accept most major insurance plans and offer clear pricing for self pay patients. When you need urgent care, we are close by and open every single day of the year.</p>
  <div class="abs rule"></div>
  <h2 class="abs solution-title">Our free standing ER solution provided</h2>
  <ul class="abs features">
    <li><svg width="14" height="14" viewBox="0 0 14 14"><circle cx="7" cy="7" r="7" fill="#333"/><path d="M4 7l2 2 4-4" stroke="#fff" stroke-width="1.6" fill="none"/></svg>No wait emergency rooms!</li>
    <li><svg width="14" height="14" viewBox="0 0 14 14"><circle cx="7" cy="7" r="7" fill="#333"/><path d="M4 7l2 2 4-4" stroke="#fff" stroke-width="1.6" fill="none"/></svg>Open 24 hours a day, 7 days a week</li>
    <li><svg width="14" height="14" viewBox="0 0 14 14"><circle cx="7" cy="7" r="7" fill="#333"/><path d="M4 7l2 2 4-4" stroke="#fff" stroke-width="1.6" fill="none"/></svg>State of the art equipment and diagnosing capabilities</li>
    <li><svg width="14" height="14" viewBox="0 0 14 14"><circle cx="7" cy="7" r="7" fill="#333"/><path d="M4 7l2 2 4-4" stroke="#fff" stroke-width="1.6" fill="none"/></svg>All our doctors are trained Emergency Medicine physicians</li>
    <li><svg width="14" height="14" viewBox="0 0 14 14"><circle cx="7" cy="7" r="7" fill="#333"/><path d="M4 7l2 2 4-4" stroke="#fff" stroke-width="1.6" fill="none"/></svg>Experienced friendly nurses</li>
    <li><svg width="14" height="14" viewBox="0 0 14 14"><circle cx="7" cy="7" r="7" fill="#333"/><path d="M4 7l2 2 4-4" stroke="#fff" stroke-width="1.6" fill="none"/></svg>Onsite emergent radiology (x-rays, CAT scans, Ultrasound)</li>
    <li><svg width="14" height="14" viewBox="0 0 14 14"><circle cx="7" cy="7" r="7" fill="#333"/><path d="M4 7l2 2 4-4" stroke="#fff" stroke-width="1.6" fill="none"/></svg>Onsite emergent laboratory with result within minutes</li>
  </ul>
  <div class="abs badge">
    <div class="big">24/7</div>
    <div class="small">Emergency<br>Response</div>
  </div>
</main>

<aside>
  <div class="abs side-rule"></div>
  <h3 class="abs side-title"><svg width="18" height="18" viewBox="0 0 18 18"><rect x="1" y="3" width="16" height="12" rx="2" fill="none" stroke="#999" stroke-width="2"/><path d="M4 7h10M4 11h7" stroke="#999" stroke-width="2"/></svg>Latest News Feeds</h3>
  <div class="abs news-title">Construction nears finish on our new emergency center</div>
  <div class="abs news-date">Posted on December 10, 2011</div>
  <p class="abs copy news-text">Our team is hiring nurses and staff ahead of the winter opening. Learn more about open roles.</p>
  <div class="abs read-more">Read more</div>
  <div class="abs map" role="img" aria-label="Street map showing the emergency center location"></div>
  <h3 class="abs side-title" style="top:796px"><svg width="18" height="18" viewBox="0 0 18 18"><path d="M3 2h9l3 3v11H3z" fill="none" stroke="#999" stroke-width="2"/><path d="M6 8h6M6 12h6" stroke="#999" stroke-width="2"/></svg>Register for updates</h3>
  <div class="abs field name">Name*</div>
  <div class="abs field mail">Email address here*</div>
  <div class="abs submit">Submit</div>
</aside>

<footer>
  <div class="abs footer-links">Home<span>|</span>About Us<span>|</span>Services<span>|</span>FAQ<span>|</span>Contact Location<span>|</span>For Provider</div>
  <div class="abs copyright">Copyright © 2011 CEDARBROOK.example, All rights reserved</div>
</footer>

</body>
</html>
```